Property Investment eBook Cover

I am a long established Australian property investment adviser, analyst and consultant who is now in semi-retired mode and have re-branded to reflect a more casual and personal approach to advising my property investor clients. I am writing a 'revised edition' to a book written in partnership with my father 20 years ago and need an eBook Cover for this new edition. The eBook will be uploaded to all the regular Australian providers (Larkfield Reader, Quince Folio, Tavi, Pagemarten)

The 3 key elements in the book cover are:

Title: The Harvest Engine of Land. The word 'Property' should be larger and more prominent. eg "The Wealth Power of" could be 1/3 the size of "Property" - with both justified left

Edition: Sydney 2021. "Sydney 2021" should be the focus and dominant imagery of the eBook cover and more prominent than the Title or Author

Author: Colin Marsh, The Housing Ledger Guide. The word "Author" should not appear. "The Housing Ledger Guide" should appear underneath Colin Marsh and justified to Colin Marsh, therefore a smaller font.

The cover should be simple, but eye-catching. No property images, more of an abstract background, than a background with an image. Our preferred colour palette is more blues/greens. Prefer SerifFonts

Copy of book published 20 years ago attached for reference only

```html
<!DOCTYPE html>
<html lang="en">
<head>
<meta charset="utf-8">
<title>The Harvest Engine of Land — Sydney 2021 Edition</title>
<link rel="stylesheet" href="https://fonts.googleapis.com/css2?family=Noto+Serif:wght@400;700&family=Ubuntu:wght@400&display=swap">
<style>
  :root {
    --paper: #fcfde8;
    --lime: #44ff00;
    --leaf: #36d934;
    --sea: #2fad6a;
    --teal: #26879a;
    --cobalt: #1f5bcc;
    --electric: #1a31ff;
  }
  * { margin: 0; padding: 0; box-sizing: border-box; }
  html, body { width: 800px; height: 1200px; overflow: hidden; background: var(--paper); }
  .cover { position: relative; width: 800px; height: 1200px; background: var(--paper); overflow: hidden; }

  .band { position: absolute; left: 0; width: 254px; height: 57px; background: var(--lime); box-shadow: 2px 2px 4px rgba(0,0,0,0.12); }
  .band--top { top: 50px; }
  .band--bottom { top: 1092px; }

  .feature-block {
    position: absolute; left: 0; top: 259px; width: 254px; height: 681px;
    background: linear-gradient(180deg, var(--lime) 0%, var(--sea) 35%, var(--teal) 60%, var(--cobalt) 80%, var(--electric) 100%);
    box-shadow: 2px 2px 4px rgba(0,0,0,0.12);
  }

  .title-block { font-weight: 400; }
  .title, .edition, .byline { position: absolute; white-space: nowrap; line-height: 1; }
  .title, .edition { font-family: "Noto Serif", Georgia, serif; font-weight: 400; }
  .title__lead { left: 298px; top: 421px; font-size: 38px; color: var(--lime); }
  .title__main { left: 296px; top: 452px; font-size: 78px; color: var(--lime); }
  .edition__city { left: 298px; top: 552px; font-size: 92px; font-weight: 700; color: var(--electric); }
  .edition__year { left: 296px; top: 625px; font-size: 158px; font-weight: 700; color: var(--electric); letter-spacing: -2px; }
  .edition__label { right: 169px; top: 775px; font-size: 45px; color: var(--lime); }

  .byline { font-family: "Ubuntu", "Helvetica Neue", sans-serif; color: var(--electric); left: 298px; }
  .byline__name { top: 1089px; font-size: 30px; }
  .byline__role { top: 1122px; font-size: 24px; }
</style>
</head>
<body>
<main class="cover">
  <div class="band band--top"></div>
  <div class="feature-block" role="img" aria-label="Abstract column of stacked green and blue colour bars"></div>
  <div class="band band--bottom"></div>

  <h1 class="title-block">
    <span class="title title__lead">The Harvest Engine of</span>
    <span class="title title__main">Land</span>
  </h1>
  <p class="edition edition__city">Sydney</p>
  <p class="edition edition__year">2021</p>
  <p class="edition edition__label">Edition</p>

  <p class="byline byline__name">Colin Marsh</p>
  <p class="byline byline__role">The Housing Ledger Guide</p>
</main>
</body>
</html>
```